Creative Landscape Architecture Company Needs a Creative Business Card Design

Marsh and Partners, Inc. is a landscape architecture (LA) company started in 1997 in Austin, TX. We work on large commerical projects all around the U.S. and provide land planning, site planning, landscape design and architectural renderings.

We don't want this card to look like a LA firm's business card. We are looking for a business card design that is edgy and cool to reflect the more artistic and creative side of our company. We would like our clients to think "now there's a business card unlike any other LA that I've seen before."

We would like it to be in standard 2"x3.5" format. Double sided. Full color ok. Our company logo is attached. We like the logo but would not be adverse to any variations you would like to make to it. Feel free to change it up. Typically the logo has been a light saturated orange color but its not necessary that you stick with it.

Requirements
Must have
• 1. Company name
2. individuals name
3. email address
4. cell number
5. office number
6. website: www.marshandpartners-demo.net
7. Business address
Nice to have
• Can add (but not necessary)
Personal titles such as "president" or "registered landscape architect"

```html
<!DOCTYPE html>
<html lang="en">
<head>
<meta charset="utf-8">
<title>Marsh and Partners – Business Card</title>
<link rel="stylesheet" href="https://fonts.googleapis.com/css2?family=Anton&family=Handlee&display=swap">
<style>
  :root {
    --canvas: #ffffff;
    --card-edge: #2b2b2b;
    --leaf-dark: #4a6a2c;
    --leaf-light: #95bf4d;
    --name-green: #9cc45c;
    --contact-green: #4d6a2f;
  }
  html, body {
    margin: 0;
    padding: 0;
    width: 1200px;
    height: 900px;
    overflow: hidden;
    background: var(--canvas);
  }
  .sheet {
    position: relative;
    width: 1200px;
    height: 900px;
  }
  .card {
    position: absolute;
    top: 290px;
    width: 503px;
    height: 288px;
    border: 1px solid var(--card-edge);
    background: var(--canvas);
    overflow: hidden;
    box-sizing: border-box;
  }
  .card--front { left: 65px; }
  .card--back  { left: 637px; }

  .company-name {
    margin: 0;
    font-family: "Anton", Impact, sans-serif;
    font-weight: 400;
    font-size: 24px;
    line-height: 1;
    letter-spacing: 0.6px;
    color: var(--name-green);
    white-space: nowrap;
  }
  .card--front .company-name {
    position: absolute;
    left: 12px;
    top: 38px;
  }
  .person {
    position: absolute;
    left: 12px;
    top: 74px;
    margin: 0;
    font-family: "Handlee", cursive;
    color: var(--contact-green);
  }
  .person__name {
    display: block;
    font-size: 15px;
    line-height: 20px;
    letter-spacing: 0.3px;
  }
  .person__title {
    display: block;
    font-size: 12px;
    line-height: 18px;
    letter-spacing: 0.3px;
  }
  .contact {
    position: absolute;
    left: 255px;
    top: 41px;
    margin: 0;
    font-family: "Handlee", cursive;
    font-style: normal;
    font-size: 13px;
    line-height: 20px;
    letter-spacing: 0.3px;
    color: var(--contact-green);
  }
  .contact span { display: block; white-space: nowrap; }

  .back-mark {
    position: absolute;
    left: 0;
    top: 48px;
    width: 100%;
    text-align: center;
  }
  .card--back .company-name {
    font-size: 34px;
    letter-spacing: 1px;
  }
  .website {
    display: block;
    margin-top: 10px;
    font-family: "Handlee", cursive;
    font-size: 14px;
    letter-spacing: 0.4px;
    color: var(--contact-green);
  }

  .skyline {
    position: absolute;
    left: 0;
    bottom: 0;
    width: 100%;
    height: 134px;
    background: linear-gradient(to bottom, var(--leaf-dark) 0%, var(--leaf-dark) 40%, var(--leaf-light) 100%);
  }
</style>
</head>
<body>
  <main class="sheet">
    <section class="card card--front" aria-label="Business card front">
      <h1 class="company-name">Marsh and Partners</h1>
      <p class="person">
        <span class="person__name">Elena Marsh</span>
        <span class="person__title">Registered Landscape Architect</span>
      </p>
      <address class="contact">
        <span>Office: 512 555 0148</span>
        <span>Cell: 512 555 0192</span>
        <span>4410 Cedar Lane, C118-240</span>
        <span>Austin, Texas 78745</span>
        <span>info@marshandpartners-demo.net</span>
      </address>
      <div class="skyline" role="img" aria-label="Green silhouette of a city skyline in front of a row of tree canopies"></div>
    </section>

    <section class="card card--back" aria-label="Business card back">
      <div class="back-mark">
        <h2 class="company-name">Marsh and Partners</h2>
        <span class="website">www.marshandpartners-demo.net</span>
      </div>
      <div class="skyline" role="img" aria-label="Green silhouette of a city skyline in front of a row of tree canopies"></div>
    </section>
  </main>
</body>
</html>
```